contemporary upscale hair salon

we need a business card design for a modern upscale salon. I would like the card to be vertical, simple, and easy to read. I would like a black matte finish on the info side with white on the back of the card, white lettering with a splash of red incorporated somewhere in there. I also want to incorporate embossing and/or cut out in the letters. The info I would like; Name of the business (Velora Salon) stylist name (Janet) phone number(4075319264) and web address (www.veloraexample.com) I am open to putting shears on the card but without it looking too cheap. Looking for something really modern and edgy. these are just ideas I have, but feel free to show me your creative ideas.
please note: the website is still under construction please do not use any images or colors off the web page. Also i currently do not have a logo, that will be a future project.

```html
<!DOCTYPE html>
<html lang="en">
<head>
<meta charset="utf-8">
<title>Velora Salon — Business Card</title>
<link rel="stylesheet" href="https://fonts.googleapis.com/css2?family=Open+Sans:wght@700&display=swap">
<style>
  :root {
    --card-black: #000000;
    --card-white: #ffffff;
    --accent-red: #ed1c24;
    --accent-red-soft: #f4777c;
  }
  html, body {
    margin: 0;
    padding: 0;
    width: 686px;
    height: 1200px;
    overflow: hidden;
    background: var(--card-black);
  }
  .card {
    position: relative;
    width: 686px;
    height: 1200px;
    background: var(--card-black);
    font-family: "Open Sans", "Helvetica Neue", Arial, sans-serif;
    color: var(--card-white);
  }
  .emblem {
    position: absolute;
    left: 0;
    top: 0;
    width: 686px;
    height: 700px;
  }
  .contact {
    position: absolute;
    left: 112px;
    top: 744px;
    margin: 0;
    font-style: normal;
  }
  .contact > * {
    display: block;
    margin: 0;
    white-space: nowrap;
    font-weight: 700;
    font-style: normal;
    text-transform: uppercase;
  }
  .salon-name {
    font-size: 56px;
    line-height: 66px;
    letter-spacing: 0.5px;
    word-spacing: 10px;
  }
  .stylist-line {
    font-size: 37px;
    line-height: 46px;
    margin-top: 2px !important;
  }
  .stylist-line .stylist,
  .stylist-line .area-code {
    margin-right: 24px;
  }
  .web-address {
    font-size: 24px;
    line-height: 34px;
    letter-spacing: 2.6px;
    margin-top: 6px !important;
  }
</style>
</head>
<body>
  <main class="card">
    <svg class="emblem" viewBox="0 0 686 700" xmlns="http://www.w3.org/2000/svg">
      <defs>
        <linearGradient id="shears-tone" x1="0" y1="0" x2="0" y2="1">
          <stop offset="0" stop-color="var(--accent-red)"/>
          <stop offset="1" stop-color="var(--accent-red-soft)"/>
        </linearGradient>
      </defs>
      <circle class="emblem-disc" cx="343" cy="390" r="233" fill="var(--card-white)"/>
      <rect class="shears-artwork" role="img" aria-label="Red open shears illustration"
            x="233" y="221" width="200" height="355" rx="18" fill="url(#shears-tone)"/>
    </svg>

    <address class="contact">
      <h1 class="salon-name">Velora Salon</h1>
      <p class="stylist-line"><span class="stylist">Janet</span><span class="area-code">(407)</span><span class="number">531-9264</span></p>
      <p class="web-address">www.veloraexample.com</p>
    </address>
  </main>
</body>
</html>
```